Larkfield Institute Logo & Business card

Larkfield Institute - Larkfield Institute
business is a training center.
Logo and business card that have an ID.
bold publicity, distinct, and prestige image
"Ensure professional Success"
that will attract target customer to come and take a look. that will look prestige on certificate after graduation, that will serve as a business tool to attract Business and enterprise customer (let them send their staff for training)
Updates

upgrade to with logo vector design

Target Market(s)

young professionals, university students, youth building career in IT fields

Industry/Entity Type

Education

Contact Information for Business Card

Address
Phone
email
Facebook

Font styles to use
Sans Serif

Colors

Designer to choose colors to be used in the design.

Requirements
Must have
• Logo Identity
• uniqueness
Nice to have
• catch phrase or illustration
Should not have
• just use alphabet as logo.

```html
<!DOCTYPE html>
<html lang="en">
<head>
<meta charset="utf-8">
<title>Larkfield Institute – Business Card</title>
<link rel="stylesheet" href="https://fonts.googleapis.com/css2?family=Work+Sans:wght@400;500;600&display=swap">
<style>
  :root {
    --backdrop: #1b1b1b;
    --card: #262626;
    --brand-blue: #2f55b5;
    --brand-teal: #2aa7a8;
    --ink-light: #f1f1f1;
    --icon: #3c63c4;
  }
  * { margin: 0; padding: 0; box-sizing: border-box; }
  html, body { width: 1200px; height: 900px; overflow: hidden; }
  body {
    background: var(--backdrop);
    font-family: "Work Sans", Arial, sans-serif;
    display: flex;
    flex-direction: column;
    align-items: center;
    justify-content: center;
    gap: 40px;
  }
  .card {
    width: 700px;
    height: 400px;
    background: var(--card);
    position: relative;
    box-shadow: 0 10px 30px rgba(0,0,0,.5);
  }
  .card--front {
    display: flex;
    align-items: center;
    justify-content: center;
  }
  .brand {
    display: flex;
    align-items: center;
    gap: 12px;
    color: var(--brand-teal);
    font-weight: 600;
    text-transform: uppercase;
    letter-spacing: 2px;
    white-space: nowrap;
  }
  .brand__dot {
    width: 22px; height: 22px;
    border-radius: 50%;
    background: var(--brand-teal);
    flex: none;
  }
  .card--front .brand__name { font-size: 34px; }
  .card--back .brand {
    position: absolute;
    left: 34px; top: 0; bottom: 0;
    width: 340px;
    letter-spacing: 1px;
  }
  .card--back .brand__dot { width: 18px; height: 18px; }
  .card--back .brand__name { font-size: 21px; }
  .divider {
    position: absolute;
    left: 398px; top: 100px;
    width: 2px; height: 215px;
    background: var(--brand-blue);
  }
  .contact {
    position: absolute;
    left: 428px; top: 100px;
    color: var(--ink-light);
  }
  .contact__name {
    color: var(--brand-blue);
    font-size: 26px;
    font-weight: 500;
    text-transform: uppercase;
    letter-spacing: 1px;
    line-height: 1;
  }
  .contact__role { font-size: 17px; margin: 8px 0 16px; }
  .contact__address { font-size: 17px; line-height: 1.35; margin-bottom: 12px; }
  .contact__list { list-style: none; font-size: 17px; line-height: 1.6; }
  .contact__list li { display: flex; align-items: center; gap: 10px; }
  .contact__list svg { width: 13px; height: 13px; flex: none; }
  .contact__web { font-weight: 600; }
</style>
</head>
<body>
  <section class="card card--front">
    <div class="brand">
      <span class="brand__dot"></span>
      <span class="brand__name">Larkfield Institute</span>
    </div>
  </section>

  <section class="card card--back">
    <div class="brand">
      <span class="brand__dot"></span>
      <span class="brand__name">Larkfield Institute</span>
    </div>
    <div class="divider"></div>
    <div class="contact">
      <p class="contact__name">Dana Whitlock</p>
      <p class="contact__role">Director</p>
      <p class="contact__address">48 Alder Row<br>Easton, MA 02375</p>
      <ul class="contact__list">
        <li><svg viewBox="0 0 16 16"><path d="M4 1 L6.5 4.5 L5 6.5 Q6.5 9.5 9.5 11 L11.5 9.5 L15 12 L13 15 Q5 14 1 3 Z" fill="var(--icon)"/></svg>508-555-0142</li>
        <li><svg viewBox="0 0 16 16"><rect x="4" y="1" width="8" height="14" rx="1.5" fill="none" stroke="var(--icon)" stroke-width="1.6"/></svg>508-555-0187</li>
        <li><svg viewBox="0 0 16 16"><rect x="1" y="3" width="14" height="10" fill="none" stroke="var(--icon)" stroke-width="1.5"/><path d="M1 3 L8 9 L15 3" fill="none" stroke="var(--icon)" stroke-width="1.5"/></svg>hello@larkfield.edu</li>
        <li class="contact__web"><svg viewBox="0 0 16 16"><circle cx="8" cy="8" r="6.5" fill="none" stroke="var(--icon)" stroke-width="1.4"/><ellipse cx="8" cy="8" rx="3" ry="6.5" fill="none" stroke="var(--icon)" stroke-width="1.2"/><path d="M1.5 8 H14.5" stroke="var(--icon)" stroke-width="1.2"/></svg>www.larkfield.edu</li>
      </ul>
    </div>
  </section>
</body>
</html>
```